Corporate Profile, with ALOT more work for winning bidder

We need
1. CD designed
2. CD Cover Designed
3. 2x Envelope's designed
4. Letter head designed
The designer picked will also get many further projects from us. Almost totaling 10k a year.
- More info
• Software installation disc
a. Logo
b. Contact details (See below)
c. Instructions
o “Please insert CD into computer and follow the prompts”
d. Title
o “Free Software Installation Disc”
• CD Sleave double sided
- Front
o Logo
o Website Address
o Facebook address
o Title
? “Free Software Installation Disc”
• Letter head
- Logo
- Contact information
- A4 paper size
• C4 Envelope
- Nicely Designed with logo
- A window to put address
- Printed return address (See below) on back
• DL Envelope, to return to us
- Had our return address ( See below)
- Nice design
Contact details
Pixel Harbour Co
17b Tamsin Crescent Bayswater, Vic, 3153
www.PixelHarbourCo.com.au
1300 42 19 58
www.Chatterloop.com/PixelHarbourCo
Return Address
Pixel Harbour Co
17b Tamsin Crescent
Bayswater, Vic, 3153

```html
<!DOCTYPE html>
<html lang="en">
<head>
<meta charset="utf-8">
<title>Pixel Harbour Co – C4 Envelope Front</title>
<link rel="stylesheet" href="https://fonts.googleapis.com/css2?family=Open+Sans:wght@400&family=Varela+Round&display=swap">
<style>
  :root {
    --page-bg: #ffffff;
    --envelope-base: #717174;
    --envelope-flap: #58585a;
    --window-fill: #e1e2e4;
    --window-edge: #3a3a3c;
    --brand-blue: #1db3e8;
    --caption-grey: #9d9d9d;
  }
  html, body {
    margin: 0;
    padding: 0;
    width: 851px;
    height: 1200px;
    overflow: hidden;
    background: var(--page-bg);
  }
  .sheet {
    position: relative;
    width: 851px;
    height: 1200px;
  }
  .envelope {
    position: absolute;
    left: 97px;
    top: 133px;
    width: 657px;
    height: 929px;
    box-shadow: 2px 2px 6px rgba(0, 0, 0, 0.25);
  }
  .envelope svg {
    display: block;
  }
  .brand-name {
    position: absolute;
    right: 44px;
    bottom: 34px;
    margin: 0;
    font-family: "Varela Round", "Nunito", sans-serif;
    font-weight: 400;
    font-size: 31px;
    letter-spacing: 0.5px;
    color: var(--brand-blue);
    white-space: nowrap;
  }
  .caption {
    position: absolute;
    left: 100px;
    top: 1084px;
    margin: 0;
    font-family: "Open Sans", Arial, sans-serif;
    font-size: 19px;
    color: var(--caption-grey);
  }
</style>
</head>
<body>
<main class="sheet">
  <section class="envelope" aria-label="C4 envelope front">
    <svg width="657" height="929" viewBox="0 0 657 929" xmlns="http://www.w3.org/2000/svg">
      <defs>
        <filter id="flap-shadow" x="-10%" y="-10%" width="130%" height="130%">
          <feDropShadow dx="2" dy="3" stdDeviation="3" flood-color="#000" flood-opacity="0.45"/>
        </filter>
      </defs>
      <rect class="envelope-base" width="657" height="929" fill="var(--envelope-base)"/>
      <path class="envelope-flap" d="M0 0 H654 A654 675 0 0 1 0 675 Z" fill="var(--envelope-flap)" filter="url(#flap-shadow)"/>
      <rect class="address-window" x="71.5" y="173.5" width="315" height="127" rx="12" fill="var(--window-fill)" stroke="var(--window-edge)" stroke-width="1"/>
    </svg>
    <p class="brand-name">Pixel Harbour Co</p>
  </section>
  <p class="caption">C4 Envelope Front</p>
</main>
</body>
</html>
```